4"x9" Roofing Flyer Design - Tile Roofing!

We are looking to create a 4"x9" double sided flyer in full color that displays pictures of before and after of tile underlayment replacement. This would have words as well.

The theme should match the overall theme of our brochure that we already have designed so they are cohesive.

I have uploaded an example of a similar flyer that we like the overall layout of.

Please read the "Design Wording" PDF I uploaded for the words and overall design layout we are looking for on this brochure.

Please let me know if you'd like more photos or anything like that.

Target Market(s)

Retirees

Industry/Entity Type

Roofing

Font styles to use
Other font styles liked:
• Match existing fonts from our brochure

Requirements
Must have
• Must match style of existing brochure (uploaded), font must match closely as well

```html
<!DOCTYPE html>
<html lang="en">
<head>
<meta charset="UTF-8">
<title>Granite Ridge Roofing – Tile Underlayment Flyer</title>
<link href="https://fonts.googleapis.com/css2?family=Lexend:wght@400;600;700&display=swap" rel="stylesheet">
<style>
  :root{
    --bg:#121312;
    --bg-soft:#1e201d;
    --olive:#6e7d1c;
    --orange:#e8561c;
    --white:#ffffff;
    --ink:#1b1b1b;
  }
  html,body{margin:0;padding:0;overflow:hidden;background:var(--bg);}
  .flyer{
    position:relative;width:1200px;height:2700px;overflow:hidden;
    background:radial-gradient(ellipse at 30% 20%,var(--bg-soft),var(--bg) 60%);
    font-family:'Lexend',sans-serif;color:var(--white);
  }
  .bands{position:absolute;inset:0;width:1200px;height:2700px;}
  .brand{position:absolute;left:0;width:1200px;text-align:center;}
  .brand-name{top:258px;font-size:82px;font-weight:700;letter-spacing:1px;}
  .brand-name .mark{display:inline-block;width:34px;height:34px;background:var(--orange);margin-right:22px;vertical-align:middle;position:relative;top:-6px;}
  .brand-phone{top:362px;font-size:80px;font-weight:700;letter-spacing:5px;}
  .photo{
    position:absolute;border:5px solid var(--orange);border-radius:44px;
    box-sizing:border-box;overflow:hidden;
  }
  .photo-a{left:47px;top:561px;width:555px;height:429px;background:linear-gradient(135deg,#8a8a84,#5a5954 55%,#3e3d39);}
  .photo-b{left:614px;top:561px;width:558px;height:429px;background:linear-gradient(180deg,#8ea4bf 0%,#c9d2db 20%,#dfe2e5 45%,#b9bfc6 100%);}
  .photo-c{left:47px;top:1039px;width:555px;height:431px;background:linear-gradient(160deg,#7a7263,#5d5446 50%,#8d8677);}
  .photo-d{left:614px;top:1044px;width:558px;height:430px;background:linear-gradient(150deg,#a08878,#8a6f5d 55%,#6f5647);}
  .tag{
    position:absolute;width:198px;height:54px;border-radius:27px;background:var(--white);
    color:var(--orange);font-size:44px;line-height:54px;text-align:center;
  }
  .tag-left{left:218px;}
  .tag-right{left:814px;}
  .tag-row1{top:537px;}
  .tag-row2{top:1017px;}
  .copy{position:absolute;left:0;width:1200px;text-align:center;letter-spacing:2px;}
  .headline{top:1530px;font-size:52px;font-weight:700;color:var(--orange);line-height:60px;letter-spacing:3px;}
  .body{font-size:36px;line-height:38px;}
  .intro{top:1658px;}
  .vintage{top:1826px;}
  .label{
    position:absolute;background:var(--white);color:var(--orange);font-weight:700;
    font-size:38px;text-align:center;letter-spacing:2px;
  }
  .label-brittle{left:399px;top:1901px;width:431px;height:62px;line-height:62px;}
  .label-compromised{left:433px;top:2130px;width:364px;height:53px;line-height:53px;}
  .brittle-text{top:1960px;line-height:45px;}
  .compromised-text{top:2180px;line-height:45px;}
  .closing{top:2364px;line-height:45px;}
  .callout{
    position:absolute;left:53px;top:2484px;width:1122px;height:179px;box-sizing:border-box;
    background:var(--white);color:var(--ink);border-radius:10px;
    font-size:36px;line-height:38px;text-align:center;letter-spacing:2px;padding-top:14px;
  }
</style>
</head>
<body>
<div class="flyer">
  <svg class="bands" viewBox="0 0 1200 2700" aria-hidden="true">
    <polygon points="0,40 0,170 1200,1180 1200,1050" fill="var(--olive)" opacity="0.28"/>
    <polygon points="0,1500 0,1600 1200,760 1200,660" fill="var(--olive)" opacity="0.22"/>
    <polygon points="0,1950 0,2060 1200,2660 1200,2550" fill="var(--olive)" opacity="0.22"/>
  </svg>

  <div class="brand brand-name"><span class="mark"></span>Granite Ridge Roofing</div>
  <div class="brand brand-phone">(555) 214-7730</div>

  <div class="photo photo-a" role="img" aria-label="Before: cracked, brittle underlayment beneath old roof tiles"></div>
  <div class="photo photo-b" role="img" aria-label="After: new synthetic underlayment installed across the roof deck"></div>
  <div class="photo photo-c" role="img" aria-label="Before: crumbling, debris-covered underlayment under tiles"></div>
  <div class="photo photo-d" role="img" aria-label="After: finished brown tile roof with new vents"></div>

  <div class="tag tag-left tag-row1">Before</div>
  <div class="tag tag-right tag-row1">After</div>
  <div class="tag tag-left tag-row2">Before</div>
  <div class="tag tag-right tag-row2">After</div>

  <div class="copy headline">THE HIDDEN CLOCK<br>TICKING UNDER YOUR TILES</div>
  <div class="copy body intro">When a tile roof is installed, the tiles themselves are<br>not waterproof—they are simply a shield.<br>The actual waterproofing is done by the felt or<br>synthetic underlayment installed beneath them.</div>
  <div class="copy body vintage">In homes of your vintage, this underlayment is now:</div>

  <div class="label label-brittle">Brittle and Chalky:</div>
  <div class="copy body brittle-text">It cracks and turns into powder under the constant<br>heat cycles, losing its<br>waterproofing integrity.</div>

  <div class="label label-compromised">Compromised:</div>
  <div class="copy body compromised-text">Even a single leak in a neighboring home means the<br>moisture risk has increased exponentially across the<br>entire block.</div>

  <div class="copy body closing">Based on the age and materials used in this specific<br>neighborhood, underlayment failure is not</div>

  <div class="callout">Waiting for a visible ceiling stain often means the<br>damage has already spread to the roof deck, rafters,<br>and interior walls. A slow leak can silently cost<br>thousands in remediation before you ever see a drop.</div>
</div>
</body>
</html>
```